varnuko.com car care product labeling with cut outs will be printed on holographic sheet.

Need to make label for eco-friendly car care products. no hazard signs.
clean and simple design minimalism
wheel cleaner
tire shiner
glass cleaner
all purpose cleaner
247x90mm
166x150mm

Target Market(s)

eco friendly car care products. europe , uae

Industry/Entity Type

car care products, eco-friendly product line

Requirements
Must have
• BW design print on holographic sheet/label .eco-friendly signs
Nice to have
• premium product look and simplicity will be at first place, can be with cut outs

```html
<!DOCTYPE html>
<html lang="en">
<head>
<meta charset="utf-8">
<title>varnuko.com – Soft Cleaner Label</title>
<link href="https://fonts.googleapis.com/css2?family=Lato:wght@400;700&display=swap" rel="stylesheet">
<style>
  :root {
    --backdrop: #dcdcdc;
    --brand-disc: #ffffff;
    --brand-ink-light: #dcdcdc;
    --label-ink: #2a2a2a;
    --seal-dark: #1f1f1f;
    --seal-ink: #f4f4f4;
    --eco-green: #3f6b4a;
    --rule: #8d8d94;
  }
  * { margin: 0; padding: 0; box-sizing: border-box; }
  html, body { width: 1200px; height: 1000px; overflow: hidden; }
  body {
    background: var(--backdrop);
    font-family: "Lato", Arial, sans-serif;
    position: relative;
  }
  .brand-disc {
    position: absolute;
    left: 122px; top: 130px;
    width: 350px; height: 350px;
    border-radius: 50%;
    background: var(--brand-disc);
    display: flex; align-items: center; justify-content: center;
  }
  .brand-disc__name {
    font-size: 76px; font-weight: 700;
    color: var(--brand-ink-light);
    letter-spacing: -1px;
  }
  .label {
    position: absolute;
    left: 850px; top: 340px;
    width: 270px; height: 630px;
    border-radius: 6px;
    background:
      linear-gradient(100deg,
        #b9c7cf 0%, #e7d3e6 12%, #f3f3f0 22%, #a9d8d2 33%,
        #d9b7d9 44%, #eef3ec 54%, #c7aac8 64%, #bfe0dc 74%,
        #f0ddec 86%, #b6c4cc 100%);
    display: flex; flex-direction: column; align-items: center;
    color: var(--label-ink);
  }
  .label__seal {
    margin-top: 136px;
    width: 94px; height: 94px; border-radius: 50%;
    background: var(--seal-dark);
    display: flex; align-items: center; justify-content: center;
  }
  .label__seal-name {
    font-size: 21px; font-weight: 700; color: var(--seal-ink);
  }
  .label__product {
    margin-top: 74px;
    font-size: 25px; font-weight: 700; letter-spacing: 0.5px;
  }
  .label__claim {
    margin-top: 70px;
    width: 222px;
    padding: 8px 0;
    border-top: 1px solid var(--rule);
    border-bottom: 1px solid var(--rule);
    font-size: 10.5px; line-height: 1.5; text-align: center;
  }
  .label__eco { margin-top: 14px; }
  .label__volume {
    margin-top: 16px;
    font-size: 17px; font-weight: 400;
  }
</style>
</head>
<body>
  <div class="brand-disc">
    <span class="brand-disc__name">varnuko</span>
  </div>

  <section class="label" aria-label="Soft Cleaner product label">
    <div class="label__seal">
      <span class="label__seal-name">varnuko</span>
    </div>
    <h1 class="label__product">SOFT CLEANER</h1>
    <p class="label__claim">Multi-action formula that moisturizes, protects and enhances the life of leather</p>
    <svg class="label__eco" width="58" height="58" viewBox="0 0 58 58" role="img" aria-label="Eco-friendly certification badge">
      <circle cx="29" cy="29" r="27" fill="none" stroke="var(--eco-green)" stroke-width="2"/>
      <circle cx="29" cy="29" r="15" fill="var(--eco-green)"/>
    </svg>
    <p class="label__volume">200 ml</p>
  </section>
</body>
</html>
```